Portfolio site - Need a basic WordPress or SquareSpace site

I need a portfolio site where I have the option to keep updating it on my own. Therefore, I'm guessing I need one that uses WordPress or SquareSpace. I just need a simple and elegant design. I'm a writer (scholarly, fiction and journalism).

Target Market(s)

Adult

Industry/Entity Type

Writer

Number of Pages Required

4 page

Font styles to use
Serif

Colors
b7a5cd
e667a6
85abd2

Requirements
Must have
• Easily updatable features. I'll have to publish links and small blurbs from time to time. And maybe the occasional image.
• Pages should be:
• Home
• Work
• Press
• Contact

```html
<!DOCTYPE html>
<html lang="en">
<head>
<meta charset="utf-8">
<title>Amira Dalton — Writer and comics scholar</title>
<link rel="stylesheet" href="https://fonts.googleapis.com/css2?family=Open+Sans:wght@400;600;700&family=Raleway:wght@500;600;700&display=swap">
<style>
:root{
  --magenta:#c83a83;
  --magenta-deep:#a92a6b;
  --pill:#9463b1;
  --lilac:#b7a5cd;
  --lilac-card:#a98bc6;
  --rose:#e667a6;
  --rose-card:#d7488f;
  --sky:#85abd2;
  --sky-card:#7096c8;
  --ink:#1c1c1c;
  --text:#444;
  --muted:#666;
  --date:#8e5bb0;
  --footer:#111;
  --footer-base:#070707;
  --white:#fff;
}
*{box-sizing:border-box;margin:0;padding:0}
html,body{width:1200px;height:2965px;overflow:hidden;background:var(--white)}
body{position:relative;font-family:"Open Sans",Arial,sans-serif;color:var(--text)}
.abs{position:absolute}

/* Header */
.header-band{left:0;top:0;width:1200px;height:419px;background:linear-gradient(180deg,var(--magenta) 0%,var(--magenta-deep) 100%)}
.nav a{position:absolute;top:50px;height:36px;line-height:36px;color:var(--white);text-decoration:none;font-size:23px;font-weight:600}
.nav .active{left:93px;width:103px;text-align:center;background:#6f8fcb;border-radius:2px}
.brand{left:436px;top:48px;font-family:"Raleway",sans-serif;font-size:28px;font-weight:600;color:var(--white);letter-spacing:1px}

/* Hero */
.hero-photo{left:89px;top:142px;width:1022px;height:445px;background:linear-gradient(100deg,#5b6f3a 0%,#8aa24c 35%,#c8d88a 60%,#7b9440 100%);box-shadow:0 6px 14px rgba(0,0,0,.25)}
.hero-pill{left:411px;top:332px;width:360px;height:133px;background:var(--pill);border-radius:66px 0 0 66px;color:var(--white);padding:28px 0 0 36px}
.hero-pill .name{font-size:40px;font-weight:600;line-height:48px}
.hero-pill .role{font-size:23px;font-weight:600;line-height:32px}
.hero-arrows{left:108px;top:548px;color:var(--white);font-size:22px;letter-spacing:14px}
.book{left:775px;top:192px;width:302px;height:480px;background:linear-gradient(135deg,#a63a2a 0%,#2d6a6a 45%,#c8a23a 80%,#7a2a2a 100%);box-shadow:8px 10px 16px rgba(0,0,0,.35);border-left:22px solid #181818}

/* About */
.about-blob{left:105px;top:766px}
.about-title{left:524px;top:790px;font-family:"Raleway",sans-serif;font-size:37px;font-weight:600;color:var(--ink)}
.about-title span{color:var(--rose-card)}
.about-text{left:524px;top:848px;width:558px;font-size:14.6px;line-height:24.8px;text-align:justify;color:var(--text)}
.btn-outline{left:524px;top:1061px;width:105px;height:32px;border:2px solid var(--rose);color:var(--rose-card);font-size:14px;line-height:28px;text-align:center}

/* Writer section */
.writer-bg{left:0;top:1243px;width:1200px;height:595px;background:radial-gradient(ellipse at 55% 40%,#45483a 0%,#2a2b22 55%,#1a1a15 100%)}
.section-title{width:1200px;left:0;text-align:center;font-family:"Raleway",sans-serif;font-weight:600;font-size:37px}
.writer-title{top:1308px;color:var(--white)}
.card{width:316px;height:301px;color:var(--white);text-align:center;padding-top:76px}
.card h3{font-family:"Raleway",sans-serif;font-size:28px;font-weight:700;letter-spacing:1px}
.card p{width:240px;margin:20px auto 0;font-size:16.5px;line-height:24px;opacity:.9}
.card .more{display:inline-block;margin-top:26px;font-size:16px;font-weight:600;padding-bottom:8px;border-bottom:3px solid var(--white)}
.card-scholar{left:99px;top:1447px;background:var(--sky-card)}
.card-fiction{left:441px;top:1451px;background:var(--rose-card)}
.card-journal{left:783px;top:1451px;background:var(--lilac-card)}
.icon-badge{width:110px;height:110px;border-radius:50%;border:4px solid var(--white)}
.badge-scholar{left:202px;top:1396px;background:var(--sky-card)}
.badge-fiction{left:543px;top:1396px;background:var(--rose-card)}
.badge-journal{left:886px;top:1396px;background:var(--lilac-card)}

/* Press */
.press-title{top:1930px;color:var(--ink)}
.press-card{width:500px;height:441px;background:var(--white);box-shadow:0 2px 8px rgba(0,0,0,.2)}
.press-one{left:89px;top:2030px}
.press-two{left:609px;top:2030px}
.press-photo{width:500px;height:235px}
.press-one .press-photo{background:linear-gradient(135deg,#1e1510 0%,#6b4522 50%,#2a1d14 100%)}
.press-two .press-photo{background:linear-gradient(135deg,#c98a2a 0%,#7a7a3a 45%,#3c4a26 100%)}
.press-body{padding:22px 38px 0}
.press-date{font-size:13px;color:var(--date);letter-spacing:.5px}
.press-body h4{margin-top:12px;font-size:20px;font-weight:400;color:var(--ink)}
.press-body p{margin-top:10px;font-size:13.3px;line-height:22px;color:var(--muted)}
.press-more{display:inline-block;margin-top:12px;font-size:13px;font-weight:600;color:var(--ink);padding-bottom:6px;border-bottom:2px solid var(--ink)}

/* Footer */
.footer-rule{left:0;top:2566px;width:1200px;height:10px;background:var(--magenta)}
.footer{left:0;top:2576px;width:1200px;height:320px;background:var(--footer);color:var(--white)}
.footer-base{left:0;top:2896px;width:1200px;height:69px;background:var(--footer-base);color:#aaa;font-size:13px;text-align:center;line-height:69px}
.footer-brand{left:87px;top:2712px;font-family:"Raleway",sans-serif;font-size:24px;font-weight:600;color:var(--white)}
.social{width:36px;height:36px;border-radius:50%;background:#2d2d2d;top:2789px}
.social.on{background:var(--pill)}
.f-head{top:2660px;font-size:20px;font-weight:400;color:var(--white)}
.f-list{font-size:15px;line-height:33px;color:#e6e6e6;list-style:none}
.contact-label{font-size:16px;font-weight:700}
.contact-line{font-size:14px;line-height:22px;color:#e6e6e6}
</style>
</head>
<body>

<div class="abs header-band"></div>
<nav class="nav">
  <a class="active" href="#">Home</a>
  <a style="left:291px" href="#">Work</a>
  <a style="left:828px" href="#">Press</a>
  <a style="left:999px" href="#">Contact</a>
</nav>
<div class="abs brand">Amira Dalton</div>

<div class="abs hero-photo" role="img" aria-label="Photo of a woman reading a book while sitting on grass under a tree in a sunny park"></div>
<div class="abs hero-pill"><div class="name">Amira Dalton</div><div class="role">Writer and comics scholar</div></div>
<div class="abs hero-arrows">‹ ›</div>
<div class="abs book" role="img" aria-label="Cover of the Harbour Lines comics anthology with a colourful illustrated dragon artwork"></div>

<svg class="abs about-blob" width="372" height="370" viewBox="0 0 372 370">
  <ellipse cx="170" cy="176" rx="166" ry="150" fill="var(--sky)" opacity=".95"/>
  <ellipse cx="200" cy="200" rx="168" ry="162" fill="var(--rose)" opacity=".75"/>
  <ellipse cx="226" cy="180" rx="140" ry="160" fill="var(--lilac)" opacity=".85" transform="rotate(-15 226 180)"/>
  <circle cx="190" cy="180" r="146" fill="#111"/>
  <circle cx="190" cy="180" r="136" fill="url(#aboutPhoto)"/>
  <defs>
    <linearGradient id="aboutPhoto" x1="0" y1="0" x2="1" y2="1">
      <stop offset="0" stop-color="#6b4a3a"/><stop offset=".5" stop-color="#9a7a5a"/><stop offset="1" stop-color="#3a3a4a"/>
    </linearGradient>
  </defs>
  <title>Portrait photo of the writer holding a comic book in a bookshop</title>
</svg>
<h2 class="abs about-title">About <span>me</span></h2>
<p class="abs about-text">Amira Dalton is a writer and comics scholar. She recently published her first short story comic, "Thousand Lakeside Nights" in the Harbour Lines Anthology which was illustrated by Lena Ortiz. As a comics scholar, her research interests are mainly focused on Muslimah and intersectional superheroes, as well as racialized women in comics. She most recently completed an audience analysis of young adult Muslim consumers of comics, and is currently working on more fiction and scholarly projects. She lives in Toronto, Ontario.</p>
<a class="abs btn-outline">Read More</a>

<div class="abs writer-bg" role="img" aria-label="Dark moody photo of trees and fallen leaves in a forest"></div>
<h2 class="abs section-title writer-title">I'm a writer</h2>

<div class="abs card card-scholar"><h3>Scholar</h3><p>It is a long established fact that a reader will be is tracted by the readable content</p><span class="more">READ MORE</span></div>
<div class="abs card card-fiction"><h3>Fiction</h3><p>It is a long established fact that a reader will be is tracted by the readable content</p><span class="more">READ MORE</span></div>
<div class="abs card card-journal"><h3>Journalism</h3><p>It is a long established fact that a reader will be is tracted by the readable content</p><span class="more">READ MORE</span></div>

<svg class="abs icon-badge badge-scholar" viewBox="0 0 110 110"><g fill="none" stroke="#fff" stroke-width="3"><rect x="36" y="32" width="38" height="48" rx="3"/><rect x="46" y="27" width="18" height="9" rx="2"/><line x1="44" y1="50" x2="66" y2="50"/><line x1="44" y1="60" x2="66" y2="60"/><line x1="44" y1="70" x2="58" y2="70"/></g></svg>
<svg class="abs icon-badge badge-fiction" viewBox="0 0 110 110"><g fill="none" stroke="#fff" stroke-width="3"><path d="M42 52a13 13 0 0 1 26 0"/><ellipse cx="55" cy="56" rx="26" ry="8"/><line x1="46" y1="66" x2="40" y2="80"/><line x1="55" y1="66" x2="55" y2="80"/><line x1="64" y1="66" x2="70" y2="80"/></g></svg>
<svg class="abs icon-badge badge-journal" viewBox="0 0 110 110"><g fill="none" stroke="#fff" stroke-width="3"><rect x="32" y="34" width="46" height="40" rx="2"/><path d="M78 44h6v26a4 4 0 0 1-8 0"/><rect x="39" y="42" width="14" height="12"/><line x1="58" y1="44" x2="71" y2="44"/><line x1="58" y1="52" x2="71" y2="52"/><line x1="39" y1="62" x2="71" y2="62"/></g></svg>

<h2 class="abs section-title press-title">Press</h2>
<article class="abs press-card press-one">
  <div class="press-photo" role="img" aria-label="Warm low-light photo of a woman reading a book"></div>
  <div class="press-body"><div class="press-date">MARCH 20, 2018</div><h4>Neque porro quisquam est qui</h4><p>Praesent elementum elit at tellus nec ultricies sit amet porttitor mattis enim In massa libero interdum nec interdum vel blandi</p><span class="press-more">READ MORE</span></div>
</article>
<article class="abs press-card press-two">
  <div class="press-photo" role="img" aria-label="Sunset photo of a woman in glasses reading a book on a park bench"></div>
  <div class="press-body"><div class="press-date">MARCH 20, 2018</div><h4>Dolorem ipsum quia dolor sit amet</h4><p>Praesent elementum elit at tellus nec ultricies sit amet porttitor mattis enim In massa libero interdum nec interdum</p><span class="press-more">READ MORE</span></div>
</article>

<div class="abs footer-rule"></div>
<footer class="abs footer"></footer>
<div class="abs footer-brand">Amira Dalton</div>
<span class="abs social" style="left:91px"></span>
<span class="abs social on" style="left:146px"></span>
<span class="abs social" style="left:201px"></span>
<span class="abs social" style="left:257px"></span>

<h5 class="abs f-head" style="left:447px">CONTACT US</h5>
<svg class="abs" style="left:445px;top:2714px" width="22" height="16" viewBox="0 0 22 16"><g fill="none" stroke="#ddd" stroke-width="1.5"><rect x="1" y="1" width="20" height="14"/><path d="M1 1l10 8 10-8"/></g></svg>
<div class="abs" style="left:475px;top:2706px">
  <div class="contact-label">Email id</div>
  <div class="contact-line">hello@amiradalton.com</div>
  <div class="contact-line">@amirawrites</div>
</div>
<svg class="abs" style="left:445px;top:2788px" width="20" height="20" viewBox="0 0 20 20"><path d="M4 1l4 4-2 3a11 11 0 0 0 6 6l3-2 4 4-3 3C8 19 1 12 1 4z" fill="none" stroke="#ddd" stroke-width="1.5"/></svg>
<div class="abs" style="left:475px;top:2786px">
  <div class="contact-label">PHONE NUMBER</div>
  <div class="contact-line">(08) 5550 0142</div>
</div>

<h5 class="abs f-head" style="left:761px">ABOUT</h5>
<ul class="abs f-list" style="left:763px;top:2701px"><li>Home</li><li>About Us</li><li>Work</li><li>Help us</li></ul>
<h5 class="abs f-head" style="left:981px">RESOURCES</h5>
<ul class="abs f-list" style="left:983px;top:2701px"><li>Writings</li><li>Press</li><li>Testimonials</li><li>FAQ</li></ul>

<div class="abs footer-base">© 2018 Company Name&nbsp; All right reserved</div>
</body>
</html>
```